St Louis Electrician Needing a Business Card Design!!

We are a St Louis based electrical contracting firm that needs help designing a business card. We have a logo and I have another image that I would like to incorporate. Open to ideas..Thanks!!

Industry/Entity Type

Business

Requirements
Must have
• there are two downloads...one is the logo and the other is what i was wanting coming off the logo...the light rays. Like the logo with the blue background...Was thinking the whole card would be that color blue.
Should not have
• No lightning bolts

```html
<!DOCTYPE html>
<html lang="en">
<head>
<meta charset="utf-8">
<title>Brightline Electric Inc. — Business Card</title>
<link rel="stylesheet" href="https://fonts.googleapis.com/css2?family=Marcellus&display=swap">
<style>
  :root {
    --card-blue: #1f3f7c;
    --card-blue-deep: #1b3872;
    --ray-blue: #3f73a8;
    --glow-white: #f4f5fb;
    --glow-lilac: #b9b6dc;
    --name-white: #ffffff;
  }

  html, body {
    margin: 0;
    padding: 0;
    width: 1200px;
    height: 699px;
    overflow: hidden;
    background: var(--card-blue);
  }

  .card {
    position: relative;
    width: 1200px;
    height: 699px;
    overflow: hidden;
    background: var(--card-blue);
  }

  .light-burst {
    position: absolute;
    inset: 0;
    background:
      radial-gradient(circle at 577px 403px,
        var(--glow-white) 0px,
        var(--glow-lilac) 35px,
        rgba(120, 150, 200, 0.55) 90px,
        rgba(63, 115, 168, 0.35) 220px,
        rgba(63, 115, 168, 0.12) 420px,
        rgba(31, 63, 124, 0) 640px),
      linear-gradient(var(--card-blue), var(--card-blue-deep));
  }

  .company-name {
    position: absolute;
    left: 258px;
    top: 308px;
    margin: 0;
    font-family: "Marcellus", serif;
    font-weight: 400;
    color: var(--name-white);
    line-height: 1;
  }

  .company-name .name-main {
    display: block;
    font-size: 62px;
    letter-spacing: -0.5px;
  }

  .company-name .name-suffix {
    display: block;
    margin-top: 8px;
    margin-left: 370px;
    font-size: 30px;
  }
</style>
</head>
<body>
  <main class="card">
    <div class="light-burst" role="img" aria-label="Soft white light burst with blue rays radiating across the card"></div>
    <h1 class="company-name">
      <span class="name-main">Brightline Electric</span>
      <span class="name-suffix">Inc.</span>
    </h1>
  </main>
</body>
</html>
```